Business Card design for a company called Tallow Flame NI

I need a business card design for my oil fired boiler servicing company. I have a logo design already and Im just looking that incorporated into the business card design. card details; Tallow Flame NI
Oil Burner Servicing - Mid Ulster Area
Service Engineer - Owen Marsh
Mobile 07751364927
email - Tallow.Flame.NI@hearthmail.example
www.tallowflameni.example
I carry out Servicing, Commissioning, Fault Finding, Warranty Validation
Target Market(s)
home owners with oil fired central heating
Industry/Entity Type
Business
Contact Information for Business Card
Tallow Flame NI
Tell. 07751364927
Web: www.tallowflameni.example
email Tallow.Flame.NI@Hearthmail.Example
Servicing Fault Finding Commissioning Warranty Validation
Look and feel

```html
<!DOCTYPE html>
<html lang="en">
<head>
<meta charset="utf-8">
<title>Tallow Flame NI – Business Card</title>
<link rel="stylesheet" href="https://fonts.googleapis.com/css2?family=Ubuntu:ital,wght@0,400;0,700;1,400&display=swap">
<style>
  :root {
    --page-bg: #e7e5e2;
    --card-top: #f7f8f6;
    --card-top-shade: #e9ecea;
    --brand-green: #3f9c2c;
    --band-green-dark: #2f8a24;
    --band-green-light: #74c043;
    --band-text: #ffffff;
    --band-text-soft: #e9f5e2;
    --strip-bg: #4b4d4c;
    --strip-text: #d9dbd9;
  }
  * { margin: 0; padding: 0; box-sizing: border-box; }
  html, body {
    width: 1200px;
    height: 969px;
    overflow: hidden;
    background: var(--page-bg);
    font-family: "Ubuntu", Arial, sans-serif;
  }
  .business-card {
    position: absolute;
    left: 100px;
    top: 200px;
    width: 1000px;
    height: 570px;
    border-radius: 30px;
    overflow: hidden;
    background: linear-gradient(180deg, var(--card-top) 0%, var(--card-top-shade) 100%);
    box-shadow: 0 18px 40px rgba(0,0,0,0.18);
  }
  .brand-header { position: absolute; left: 57px; top: 55px; }
  .brand-dot {
    position: absolute;
    left: 0;
    top: 6px;
    width: 100px;
    height: 100px;
    border-radius: 50%;
    background: var(--brand-green);
  }
  .brand-name {
    position: absolute;
    left: 126px;
    top: 18px;
    white-space: nowrap;
    font-weight: 700;
    font-size: 46px;
    color: var(--brand-green);
    letter-spacing: 0.2px;
  }
  .brand-tagline {
    position: absolute;
    left: 128px;
    top: 78px;
    white-space: nowrap;
    font-weight: 700;
    font-size: 14.5px;
    letter-spacing: 1.2px;
    color: var(--brand-green);
    text-transform: uppercase;
  }
  .contact-band {
    position: absolute;
    left: 0;
    top: 215px;
    width: 100%;
    height: 300px;
    background: linear-gradient(90deg, var(--band-green-dark) 0%, #4ea831 55%, var(--band-green-light) 100%);
  }
  .person-name {
    position: absolute;
    left: 55px;
    top: 34px;
    font-size: 33px;
    font-weight: 400;
    color: var(--band-text);
  }
  .person-role {
    position: absolute;
    left: 55px;
    top: 74px;
    font-size: 27px;
    color: var(--band-text-soft);
  }
  .contact-list { position: absolute; left: 55px; top: 130px; list-style: none; }
  .contact-item {
    display: flex;
    align-items: center;
    height: 38px;
    font-size: 26px;
    color: var(--band-text);
  }
  .contact-icon { width: 26px; height: 26px; margin-right: 16px; flex: none; }
  .services-strip {
    position: absolute;
    left: 0;
    bottom: 0;
    width: 100%;
    height: 55px;
    background: var(--strip-bg);
    display: flex;
    align-items: center;
    justify-content: center;
    gap: 16px;
    font-style: italic;
    font-size: 25px;
    color: var(--strip-text);
  }
  .service-sep { font-style: normal; font-size: 18px; }
</style>
</head>
<body>
  <article class="business-card">
    <header class="brand-header">
      <span class="brand-dot"></span>
      <h1 class="brand-name">Tallow Flame NI</h1>
      <p class="brand-tagline">Oil Burner Servicing - Mid Ulster Area</p>
    </header>

    <section class="contact-band">
      <h2 class="person-name">Owen Marsh</h2>
      <p class="person-role">Service Engineer</p>
      <ul class="contact-list">
        <li class="contact-item">
          <svg class="contact-icon" viewBox="0 0 26 26" aria-hidden="true">
            <rect x="7" y="1" width="12" height="24" rx="2" fill="none" stroke="#fff" stroke-width="2.4"/>
            <circle cx="13" cy="20.5" r="1.6" fill="#fff"/>
          </svg>
          07751364927
        </li>
        <li class="contact-item">
          <svg class="contact-icon" viewBox="0 0 26 26" aria-hidden="true">
            <path d="M2 9 Q13 1 24 9 L21 12 L17 10 L17 7 Q13 5.5 9 7 L9 10 L5 12 Z" fill="#fff"/>
            <rect x="5" y="13" width="16" height="11" rx="2" fill="#fff"/>
            <circle cx="13" cy="18.5" r="3" fill="#4ea831"/>
          </svg>
          07751364927
        </li>
        <li class="contact-item">
          <svg class="contact-icon" viewBox="0 0 26 26" aria-hidden="true">
            <rect x="1" y="5" width="24" height="16" rx="1.5" fill="#fff"/>
            <path d="M2 6 L13 14 L24 6" fill="none" stroke="#4ea831" stroke-width="2"/>
          </svg>
          Tallow.Flame.NI@hearthmail.example
        </li>
        <li class="contact-item">
          <svg class="contact-icon" viewBox="0 0 26 26" aria-hidden="true">
            <circle cx="13" cy="13" r="11.5" fill="#fff"/>
            <path d="M6 8 Q10 6 11 10 Q9 13 12 15 Q11 19 8 19 Q5 14 6 8 Z M15 5 Q20 7 21 12 Q18 14 16 11 Q14 9 15 5 Z" fill="#4ea831"/>
          </svg>
          www.tallowflameni.example
        </li>
      </ul>
    </section>

    <footer class="services-strip">
      <span>Commissioning</span>
      <span class="service-sep">•</span>
      <span>Fault Finding</span>
      <span class="service-sep">•</span>
      <span>Warranty Validation</span>
    </footer>
  </article>
</body>
</html>
```